Real Estate Agent who sells beach front condos needs a template for a monthly postcard campaign.

Carla Jenrick, Homebroker with Quintavo Real Estate and Development, Licensed in Florida and Alabama, 251-468-3072, carlajenrick.example, carlamjenrick@mailbox.example. Need a postcard template which will allow me to type in recipe instructions and insert a photo of the finished food product. The recipe and photo will change every month, so I need this to be something I can easily change and reorder every month. I sell beach condos primarily. I'd like large photos of the food. Glossy card on both sides.

Target Market(s)

buyers and sellers of homes, condos, lots

Industry/Entity Type

Real Estate Agent

Requirements
Must have
• my contact information, my photo, my company name (Quintavo Real Estate and Development), the Equal Dwelling Logo, the Homebroker Logo, the statement "Contact me for all your Real Estate needs!", a template on the front side that will let me change the photograph at will, and a template on the back side that will let me type words.
Nice to have
• For my contact info and photo to stand out also.

```html
<!DOCTYPE html>
<html lang="en">
<head>
<meta charset="utf-8">
<title>Carla Jenrick – Monthly Recipe Postcard</title>
<link rel="stylesheet" href="https://fonts.googleapis.com/css2?family=Dancing+Script:wght@600;700&family=Roboto+Condensed:wght@400;700&display=swap">
<style>
  :root{
    --page:#e9e7e3;
    --mustard:#d5ae42;
    --mustard-deep:#c99f33;
    --mint:#7fe3c4;
    --teal-script:#5fd3c3;
    --ink:#1d1a14;
    --sky:#6aaee6;
    --sky-deep:#4f95d6;
    --sky-light:#8cc3ef;
    --paper:#ffffff;
    --line-blue:#5b9be0;
    --logo-brown:#8a5a2b;
    --dish-light:#ece3d0;
    --dish-warm:#d8c49a;
  }
  *{box-sizing:border-box;margin:0;padding:0}
  html,body{width:1200px;height:525px;overflow:hidden;background:var(--page)}
  body{position:relative;font-family:"Roboto Condensed",Arial,sans-serif;color:var(--ink)}

  .postcard{position:absolute;top:62px;height:445px;box-shadow:0 2px 6px rgba(0,0,0,.25);overflow:hidden}

  /* ---------- Recipe side ---------- */
  .recipe-side{left:57px;width:541px;background:linear-gradient(180deg,var(--mustard),var(--mustard-deep))}
  .dish-photo{position:absolute;left:20px;top:25px;width:345px;height:218px;border:3px solid var(--mint);
    background:linear-gradient(160deg,var(--dish-light),var(--dish-warm))}
  .agent-card{position:absolute;left:380px;top:25px;width:120px;text-align:center}
  .agent-photo{display:block;margin:0 auto;width:74px;height:86px;border:3px solid var(--mint);border-radius:6px;
    background:linear-gradient(180deg,#cbb8a0,#e3cfa8 45%,#3a3a3a)}
  .gift-line{margin-top:8px;font-weight:700;font-size:12.5px;white-space:nowrap}
  .tagline{font-size:12px;line-height:1.2}
  .agent-contact{margin-top:6px;font-size:10.5px;line-height:1.35;white-space:nowrap}
  .recipe-title{position:absolute;left:22px;top:256px;width:132px;font-family:"Dancing Script",cursive;font-weight:700;
    font-size:20px;line-height:1.18;color:var(--teal-script)}
  .ingredients{position:absolute;left:150px;top:250px;width:182px;font-size:9.4px;line-height:1.2;white-space:nowrap}
  .directions{position:absolute;left:333px;top:250px;width:200px;font-size:9.4px;line-height:1.2}
  .recipe-heading{font-weight:700;font-size:10.5px;margin-bottom:7px}
  .directions p + p{margin-top:10px}

  /* ---------- Mailing side ---------- */
  .mailer-side{left:613px;width:528px;background:var(--paper)}
  .mailer-panel{position:absolute;left:0;top:0;width:279px;height:100%;
    background:radial-gradient(ellipse at 30% 70%,var(--sky-light),transparent 60%),linear-gradient(160deg,var(--sky),var(--sky-deep))}
  .mailer-photo{position:absolute;left:84px;top:35px;width:113px;height:128px;border:3px solid var(--paper);
    background:linear-gradient(180deg,#d8ccb5,#e6d2a6 45%,#2f2f2f)}
  .agent-name{position:absolute;left:54px;top:170px;font-family:"Dancing Script",cursive;font-weight:700;font-size:34px;color:var(--paper);line-height:1}
  .agent-role{position:absolute;left:54px;top:204px;font-family:"Dancing Script",cursive;font-weight:700;font-size:17px;line-height:1;color:var(--paper);white-space:nowrap}
  .license{position:absolute;left:62px;top:228px;font-size:10.5px;color:var(--paper)}
  .company{position:absolute;left:50px;top:250px;font-weight:700;font-size:12.5px;text-shadow:0 0 3px #fff}
  .call-to-action{position:absolute;left:50px;top:280px;font-family:"Dancing Script",cursive;font-weight:700;font-size:19px;line-height:1.05;color:var(--paper)}
  .mailer-contact{position:absolute;left:76px;top:323px;font-size:11px;line-height:1.25}
  .mailer-contact .phone{font-size:15px;font-weight:700;display:flex;align-items:center;gap:4px}

  .return-label{position:absolute;left:317px;top:28px;width:123px;height:60px;background:var(--sky-light);color:var(--paper);text-align:center}
  .return-label .name{font-family:"Dancing Script",cursive;font-weight:700;font-size:19px;line-height:1;padding-top:4px}
  .return-label .role{font-family:"Dancing Script",cursive;font-weight:700;font-size:11px}
  .return-label .lic{font-size:7.5px;margin-top:3px}
  .stamp-box{position:absolute;left:452px;top:28px;width:62px;height:62px;border:2px solid var(--line-blue)}
  .address-lines{position:absolute;left:317px;top:175px;width:198px}
  .address-lines span{display:block;height:24px;border-bottom:1.5px solid var(--line-blue)}
  .address-lines span:first-child{height:0}
  .badges{position:absolute;left:323px;top:340px;display:flex;align-items:center;gap:14px}
  .company-mark{font-size:11px;color:var(--logo-brown);display:flex;align-items:center;gap:4px}
  .company-mark i{width:10px;height:10px;background:var(--logo-brown)}
  .badge-shape{width:22px;height:22px;background:var(--ink)}
  .homebroker-mark{font-size:9px;display:flex;align-items:center;gap:4px}
  .homebroker-mark i{width:16px;height:16px;background:var(--ink)}
</style>
</head>
<body>

<section class="postcard recipe-side">
  <div class="dish-photo" role="img" aria-label="Photo of the month's finished dish: linguine with shrimp, spinach and tomatoes"></div>
  <div class="agent-card">
    <div class="agent-photo" role="img" aria-label="Headshot of Carla Jenrick"></div>
    <p class="gift-line">A gift from Carla Jenrick</p>
    <p class="tagline">Your Recipe for Success<br>In Real Estate</p>
    <p class="agent-contact">✆251.468.3072<br>E: carlamjenrick@mailbox.example</p>
  </div>
  <h2 class="recipe-title">Linguine with Shrimp, Garlic, Baby Spinach, and Tomatoes</h2>
  <div class="ingredients">
    <h3 class="recipe-heading">Ingredients:</h3>
    1 lb linguine<br>
    3 tbsp extra virgin olive oil<br>
    1 pound shrimp<br>
    1 tsp Harborline seasoning<br>
    1/4 tsp crushed red pepper flakes<br>
    3 cloves minced garlic<br>
    2 big handfuls of baby spinach leaves<br>
    3 on-the-vine ripe or heirloom tomatoes, diced<br>
    parmigiano reggiano for grating on top
  </div>
  <div class="directions">
    <h3 class="recipe-heading">Directions:</h3>
    <p>Cook the linguine according to the directions listed above. Drain the pasta, and immediately toss it with the 3 tbsp extra virgin olive oil, baby spinach, and tomatoes. The residual heat from the pasta will cook the tomatoes and spinach ever so slightly and take the raw edge off.</p>
    <p>Saute the shrimp with the garlic, Harborline, red pepper flakes, and toss it with your pasta. Grate some parmigiano on top. Enjoy!</p>
  </div>
</section>

<section class="postcard mailer-side">
  <div class="mailer-panel">
    <div class="mailer-photo" role="img" aria-label="Headshot of Carla Jenrick"></div>
    <p class="agent-name">Carla Jenrick</p>
    <p class="agent-role">Your Gulf Coast Homebroker</p>
    <p class="license">Licensed in Alabama &amp; Florida</p>
    <p class="company">Quintavo Real Estate &amp; Development</p>
    <p class="call-to-action">Contact me for all your<br>Real Estate needs!</p>
    <div class="mailer-contact">
      <p class="phone">
        <svg width="14" height="14" viewBox="0 0 24 24" aria-hidden="true"><circle cx="12" cy="12" r="10.5" fill="none" stroke="#1d1a14" stroke-width="2"/><path d="M8.5 6.5l2 2.5-1.2 1.4c.8 1.7 2 2.9 3.6 3.7l1.4-1.2 2.5 2-1.3 1.8c-3.8-.6-7.2-4-7.8-7.9z" fill="#1d1a14"/></svg>
        251.468.3072
      </p>
      <p>E: carlamjenrick@mailbox.example</p>
      <p>carlajenrick.example</p>
    </div>
  </div>

  <div class="return-label">
    <p class="name">Carla Jenrick</p>
    <p class="role">Your Gulf Coast Homebroker</p>
    <p class="lic">Licensed in Alabama &amp; Florida</p>
  </div>
  <div class="stamp-box"></div>
  <div class="address-lines"><span></span><span></span><span></span><span></span></div>

  <div class="badges">
    <span class="company-mark"><i></i>Quintavo</span>
    <span class="badge-shape" role="img" aria-label="Equal Dwelling Logo"></span>
    <span class="homebroker-mark" role="img" aria-label="Homebroker Logo"><i></i>Homebroker</span>
  </div>
</section>

</body>
</html>
```